Design for a 170 ml Dessert Cup (Ice Cream / Fruits / Creams)

About Us
We are a small start-up from Switzerland focused on sustainable to-go and street food packaging products, all made with FSC-certified materials. Our name is: marigold lattice - you will find our logo attached.
Our success is strongly driven by the design of our packaging — we position ourselves as a premium brand, offering unique, creative, and stylish designs that stand out from the competition.

Project Overview
We are launching a new product: a dessert cup (170 ml) that will represent our brand's spirit and values.
The design should be simple, beautiful, fresh, cheerful, modern, sweet, and trendy.
Even though this will be used mainly for ice cream, it should also work for fruits, creams, and other desserts. Therefore, please do not include any literal ice cream visuals (eg scoops, cones, flavors).
In the future, we plan to introduce other cup sizes — so the design should be flexible enough to work across different sizes by changing the color scheme (same design, different colors).
For now, we focus on finding the main design for the 170 ml size (approx. 8 cm diameter x 4 cm height).

goal
Create a fun, stylish, and modern design for our 170 ml dessert cup that stands out on the shelf and connects emotionally with customers. Please use the template of the cup (document attached).
Colors should be bright and lively, but not too strong or harsh.
We also like patterns that repeat themselves, simple but stylish.
Sustainability doesn't need to be the main visual theme — creativity and appeal are more important.
If it fits naturally, you may integrate the word “Marigold” (our brand name), but it's optional and should not dominate the design.

Creative Direction/Design Ideas
• Funky & Trendy: playful typography and modern patterns, simple
• Creative & Unique: abstract or quirky elements inspired by desserts, fruits, or textures
• High-Quality & Foody: evoke a sense of taste and indulgence, without showing ice cream directly
• Modern Aesthetics: clean, balanced layouts with simplicity
• Sweet & Soft: pastel or soft color palettes, light and fresh feeling
• You will find some pictures of designs we like attached
Technical Details
• Cup size: 170 ml (8 cm diameter × 4 cm height)
• Design should be easy to recolor for future cup sizes
• You can find the template in the documents of the project

Key Messages
• Quality • Simple • Craving
• Modern • Soft • Fun

Tone & Emotion
The design should feel happy, fresh, and delightful

Target Market(s)

Wholesale markets and small businesses (restaurants, food trucks, ice cream trucks)

Industry/Entity Type

Food Service , Restaurants

Requirements
Must have
• high quality design, simple but fun and beautiful
Should not have
• not a lot of words or no words

```html
<!DOCTYPE html>
<html lang="en">
<head>
<meta charset="utf-8">
<title>Marigold Lattice – Dessert Cup Colour Variations</title>
<link rel="stylesheet" href="https://fonts.googleapis.com/css2?family=Rubik:wght@500;600&family=Lato:ital,wght@0,400;0,700;1,400&display=swap">
<style>
  :root{
    --ink:#1a1a1a;
    --bleed-red:#e2342d;
    --text-green:#5ab54b;
    --fold-red:#c9302c;
    --paste-green:#3aa84a;
    --paper:#ffffff;
    --v1a:#9dd28a;--v1b:#96d8e6;--v1c:#98a8d6;--v1d:#f49b9b;--v1e:#f07fb5;
    --v2a:#13bba8;--v2b:#49c3d0;--v2c:#e0e01c;--v2d:#f2885a;--v2e:#ee5a8f;
    --v3a:#f07660;--v3b:#ee6278;--v3c:#e64b83;--v3d:#c4308a;--v3e:#92278f;
    --v4a:#45a4dc;--v4b:#74c25c;--v4c:#f7ec57;--v4d:#f8ac44;--v4e:#ee3758;
    --v5a:#7b71b8;--v5b:#f7eaf4;--v5c:#f05d5e;--v5d:#fed47e;--v5e:#2e9a8e;
  }
  *{margin:0;padding:0;box-sizing:border-box}
  html,body{width:1200px;height:3110px;overflow:hidden;background:var(--paper)}
  body{position:relative;font-family:'Lato',sans-serif;color:var(--ink)}
  .sheet-header{position:absolute;top:12px;left:0;width:1200px;display:flex;justify-content:center;align-items:center;gap:12px}
  .brand{display:flex;align-items:center;gap:6px;font-family:'Rubik',sans-serif;font-weight:600;font-size:15px;color:var(--ink)}
  .brand-dot{width:12px;height:12px;border-radius:50%;background:var(--ink)}
  .sheet-title{font-family:'Rubik',sans-serif;font-weight:600;font-size:36px;letter-spacing:.2px}
  .variation{position:absolute;left:0;width:1200px;height:588px}
  .variation svg{display:block}
  .t-title{font-family:'Rubik',sans-serif;font-weight:500;font-size:16px;fill:var(--ink)}
  .t-label{font-size:7.5px}
  .t-bleed{fill:var(--bleed-red)}
  .t-cut{fill:var(--ink)}
  .t-text{fill:var(--text-green)}
  .t-micro{font-size:4.5px;fill:var(--ink)}
  .t-spec{font-family:'Rubik',sans-serif;font-weight:500;font-size:9.5px;fill:var(--ink);text-anchor:middle}
  .t-legend{font-family:'Rubik',sans-serif;font-weight:500;font-size:7.5px}
  .t-pill{font-size:4.5px;font-weight:700;fill:var(--ink);text-anchor:middle}
  .t-palette{font-family:'Rubik',sans-serif;font-weight:500;font-size:7.5px;fill:var(--ink);text-anchor:middle}
  .cut-line{fill:none;stroke:var(--ink);stroke-width:.9}
  .bleed-edge{fill:none;stroke:#f27a9a;stroke-width:.8;stroke-dasharray:3 2}
  .text-area{fill:none;stroke:#bfe3b5;stroke-width:.5;stroke-dasharray:2 2}
  .fold-line{fill:none;stroke:var(--fold-red);stroke-width:.7}
  .paste-line{fill:none;stroke:var(--paste-green);stroke-width:.7}
  .lead-bleed{stroke:var(--bleed-red);stroke-width:.5}
  .lead-cut{stroke:var(--ink);stroke-width:.8}
  .lead-text{stroke:#bfe3b5;stroke-width:.5}
  .pill{fill:#fff;stroke:var(--ink);stroke-width:.6}
</style>
</head>
<body>

<header class="sheet-header">
  <div class="brand"><span class="brand-dot"></span>marigold lattice</div>
  <h1 class="sheet-title">Different Color Variation</h1>
</header>

<!-- Shared defs -->
<svg width="0" height="0" style="position:absolute">
  <defs>
    <marker id="arrow-black" markerWidth="6" markerHeight="6" refX="5" refY="3" orient="auto"><path d="M0,0 L6,3 L0,6 Z" fill="#1a1a1a"/></marker>
    <marker id="arrow-red" markerWidth="6" markerHeight="6" refX="5" refY="3" orient="auto"><path d="M0,0 L6,3 L0,6 Z" fill="#c9302c"/></marker>
    <marker id="arrow-green" markerWidth="6" markerHeight="6" refX="5" refY="3" orient="auto"><path d="M0,0 L6,3 L0,6 Z" fill="#3aa84a"/></marker>
    <linearGradient id="g1" x1="0" x2="1"><stop offset="0" stop-color="#98a8d6"/><stop offset=".25" stop-color="#f07fb5"/><stop offset=".45" stop-color="#96d8e6"/><stop offset=".6" stop-color="#f49b9b"/><stop offset=".75" stop-color="#f07fb5"/><stop offset=".9" stop-color="#96d8e6"/><stop offset="1" stop-color="#9dd28a"/></linearGradient>
    <linearGradient id="g2" x1="0" x2="1"><stop offset="0" stop-color="#13bba8"/><stop offset=".25" stop-color="#49c3d0"/><stop offset=".45" stop-color="#f2885a"/><stop offset=".6" stop-color="#ee5a8f"/><stop offset=".75" stop-color="#49c3d0"/><stop offset=".9" stop-color="#f2885a"/><stop offset="1" stop-color="#ee5a8f"/></linearGradient>
    <linearGradient id="g3" x1="0" x2="1"><stop offset="0" stop-color="#ee6278"/><stop offset=".25" stop-color="#e64b83"/><stop offset=".45" stop-color="#92278f"/><stop offset=".6" stop-color="#f07660"/><stop offset=".75" stop-color="#e64b83"/><stop offset=".9" stop-color="#92278f"/><stop offset="1" stop-color="#f07660"/></linearGradient>
    <linearGradient id="g4" x1="0" x2="1"><stop offset="0" stop-color="#45a4dc"/><stop offset=".25" stop-color="#ee3758"/><stop offset=".45" stop-color="#f8ac44"/><stop offset=".6" stop-color="#ee3758"/><stop offset=".75" stop-color="#f8ac44"/><stop offset=".9" stop-color="#ee3758"/><stop offset="1" stop-color="#f8ac44"/></linearGradient>
    <linearGradient id="g5" x1="0" x2="1"><stop offset="0" stop-color="#7b71b8"/><stop offset=".25" stop-color="#2e9a8e"/><stop offset=".45" stop-color="#fed47e"/><stop offset=".6" stop-color="#f05d5e"/><stop offset=".75" stop-color="#2e9a8e"/><stop offset=".9" stop-color="#fed47e"/><stop offset="1" stop-color="#f05d5e"/></linearGradient>
    <linearGradient id="m1" x1="0" y1="0" x2="1" y2="1"><stop offset="0" stop-color="#f49b9b"/><stop offset=".5" stop-color="#96d8e6"/><stop offset="1" stop-color="#f07fb5"/></linearGradient>
    <linearGradient id="m2" x1="0" y1="0" x2="1" y2="1"><stop offset="0" stop-color="#f2885a"/><stop offset=".5" stop-color="#49c3d0"/><stop offset="1" stop-color="#13bba8"/></linearGradient>
    <linearGradient id="m3" x1="0" y1="0" x2="1" y2="1"><stop offset="0" stop-color="#e64b83"/><stop offset=".5" stop-color="#92278f"/><stop offset="1" stop-color="#f07660"/></linearGradient>
    <linearGradient id="m4" x1="0" y1="0" x2="1" y2="1"><stop offset="0" stop-color="#ee3758"/><stop offset=".5" stop-color="#f8ac44"/><stop offset="1" stop-color="#f7ec57"/></linearGradient>
    <linearGradient id="m5" x1="0" y1="0" x2="1" y2="1"><stop offset="0" stop-color="#2e9a8e"/><stop offset=".5" stop-color="#fed47e"/><stop offset="1" stop-color="#f05d5e"/></linearGradient>
  </defs>
</svg>

<!-- Variation 01 -->
<section class="variation" style="top:96px">
<svg width="1200" height="588" viewBox="0 80 1000 490">
  <g class="dieline">
    <text class="t-label t-bleed" x="60" y="101">Area di abbondanza/ <tspan font-style="italic">Background area</tspan></text>
    <text class="t-label t-cut" x="80" y="124">Linea di taglio/ <tspan font-style="italic">Cut line</tspan></text>
    <text class="t-label t-text" x="101" y="148">Area limite del testo/ <tspan font-style="italic">Text area</tspan></text>
    <text class="t-title" x="281" y="106">Color Variation -01</text>
    <line class="lead-bleed" x1="61" y1="104" x2="61" y2="168"/>
    <line class="lead-cut" x1="80" y1="127" x2="80" y2="176"/>
    <line class="lead-text" x1="101" y1="151" x2="101" y2="182"/>
    <rect x="43" y="168" width="571" height="115" fill="url(#g1)" role="img" aria-label="Flat cup wrap with pastel geometric shapes and dot and grid textures"/>
    <rect class="bleed-edge" x="43" y="168" width="571" height="115"/>
    <rect class="text-area" x="58" y="182" width="542" height="88"/>
    <rect class="cut-line" x="51" y="176" width="556" height="100"/>
    <text class="t-micro" x="216" y="293">MADE IN ITALY ▪ C03 170cc G000000 PAPER</text>
    <path d="M85,372 Q335,290 587,348 L548,456 Q335,410 120,472 Z" fill="url(#g1)" stroke="#1a1a1a" stroke-width=".9" role="img" aria-label="Curved cup dieline with the pastel wrap pattern"/>
    <path class="fold-line" d="M92,386 Q335,305 578,362"/>
    <path class="fold-line" d="M118,462 Q335,400 548,446"/>
    <line class="paste-line" x1="572" y1="380" x2="548" y2="446"/>
    <g transform="translate(64,395) rotate(-20)"><rect class="pill" x="-14" y="-4" width="28" height="8" rx="4"/><text class="t-pill" y="1.5">Bleed Area</text></g>
    <g transform="translate(597,345) rotate(-65)"><rect class="pill" x="-16" y="-4" width="32" height="8" rx="4"/><text class="t-pill" y="1.5">Pasting Side</text></g>
    <g transform="translate(583,474) rotate(20)"><rect class="pill" x="-22" y="-4" width="44" height="8" rx="4"/><text class="t-pill" y="1.5">Non Printed Area</text></g>
    <text class="t-spec" x="347" y="487">6 OZ ICE CREAM/Desert CUP</text>
    <text class="t-spec" x="347" y="506">170 ml</text>
    <line x1="116" y1="524" x2="172" y2="524" stroke="#1a1a1a" stroke-width=".8" marker-end="url(#arrow-black)"/>
    <text class="t-legend" x="176" y="527" fill="#1a1a1a">CUTTING LINE</text>
    <line x1="246" y1="524" x2="302" y2="524" stroke="#c9302c" stroke-width=".8" marker-end="url(#arrow-red)"/>
    <text class="t-legend" x="306" y="527" fill="#c9302c">FOLDING LINE</text>
    <line x1="380" y1="524" x2="435" y2="524" stroke="#3aa84a" stroke-width=".8" marker-end="url(#arrow-green)"/>
    <text class="t-legend" x="440" y="527" fill="#3aa84a">PASTING SIDE</text>
  </g>
  <g class="showcase">
    <rect x="768" y="122" width="165" height="234" rx="18" fill="url(#m1)" role="img" aria-label="Three stacked dessert cups wearing the pastel wrap"/>
    <text class="t-palette" x="843" y="427">Bright Pastel Color Palette</text>
    <rect x="777" y="437" width="27.5" height="91" fill="#9dd28a"/>
    <rect x="804.5" y="437" width="27.5" height="91" fill="#96d8e6"/>
    <rect x="832" y="437" width="27.5" height="91" fill="#98a8d6"/>
    <rect x="859.5" y="437" width="27.5" height="91" fill="#f49b9b"/>
    <rect x="887" y="437" width="27.5" height="91" fill="#f07fb5"/>
  </g>
</svg>
</section>

<!-- Variation 02 -->
<section class="variation" style="top:685px">
<svg width="1200" height="588" viewBox="0 80 1000 490">
  <g class="dieline">
    <text class="t-label t-bleed" x="60" y="101">Area di abbondanza/ <tspan font-style="italic">Background area</tspan></text>
    <text class="t-label t-cut" x="80" y="124">Linea di taglio/ <tspan font-style="italic">Cut line</tspan></text>
    <text class="t-label t-text" x="101" y="148">Area limite del testo/ <tspan font-style="italic">Text area</tspan></text>
    <text class="t-title" x="281" y="106">Color Variation -02</text>
    <line class="lead-bleed" x1="61" y1="104" x2="61" y2="168"/>
    <line class="lead-cut" x1="80" y1="127" x2="80" y2="176"/>
    <line class="lead-text" x1="101" y1="151" x2="101" y2="182"/>
    <rect x="43" y="168" width="571" height="115" fill="url(#g2)" role="img" aria-label="Flat cup wrap with summer pastel geometric shapes and grid textures"/>
    <rect class="bleed-edge" x="43" y="168" width="571" height="115"/>
    <rect class="text-area" x="58" y="182" width="542" height="88"/>
    <rect class="cut-line" x="51" y="176" width="556" height="100"/>
    <text class="t-micro" x="216" y="293">MADE IN ITALY ▪ C03 170cc G000000 PAPER</text>
    <path d="M85,372 Q335,290 587,348 L548,456 Q335,410 120,472 Z" fill="url(#g2)" stroke="#1a1a1a" stroke-width=".9" role="img" aria-label="Curved cup dieline with the summer pastel wrap pattern"/>
    <path class="fold-line" d="M92,386 Q335,305 578,362"/>
    <path class="fold-line" d="M118,462 Q335,400 548,446"/>
    <line class="paste-line" x1="572" y1="380" x2="548" y2="446"/>
    <g transform="translate(64,395) rotate(-20)"><rect class="pill" x="-14" y="-4" width="28" height="8" rx="4"/><text class="t-pill" y="1.5">Bleed Area</text></g>
    <g transform="translate(597,345) rotate(-65)"><rect class="pill" x="-16" y="-4" width="32" height="8" rx="4"/><text class="t-pill" y="1.5">Pasting Side</text></g>
    <g transform="translate(583,474) rotate(20)"><rect class="pill" x="-22" y="-4" width="44" height="8" rx="4"/><text class="t-pill" y="1.5">Non Printed Area</text></g>
    <text class="t-spec" x="347" y="487">6 OZ ICE CREAM/Desert CUP</text>
    <text class="t-spec" x="347" y="506">170 ml</text>
    <line x1="116" y1="524" x2="172" y2="524" stroke="#1a1a1a" stroke-width=".8" marker-end="url(#arrow-black)"/>
    <text class="t-legend" x="176" y="527" fill="#1a1a1a">CUTTING LINE</text>
    <line x1="246" y1="524" x2="302" y2="524" stroke="#c9302c" stroke-width=".8" marker-end="url(#arrow-red)"/>
    <text class="t-legend" x="306" y="527" fill="#c9302c">FOLDING LINE</text>
    <line x1="380" y1="524" x2="435" y2="524" stroke="#3aa84a" stroke-width=".8" marker-end="url(#arrow-green)"/>
    <text class="t-legend" x="440" y="527" fill="#3aa84a">PASTING SIDE</text>
  </g>
  <g class="showcase">
    <rect x="768" y="122" width="165" height="234" rx="18" fill="url(#m2)" role="img" aria-label="Three stacked dessert cups wearing the summer pastel wrap"/>
    <text class="t-palette" x="845" y="427">Bright Summer Pastel Color Palette</text>
    <rect x="777" y="437" width="27.5" height="91" fill="#13bba8"/>
    <rect x="804.5" y="437" width="27.5" height="91" fill="#49c3d0"/>
    <rect x="832" y="437" width="27.5" height="91" fill="#e0e01c"/>
    <rect x="859.5" y="437" width="27.5" height="91" fill="#f2885a"/>
    <rect x="887" y="437" width="27.5" height="91" fill="#ee5a8f"/>
  </g>
</svg>
</section>

<!-- Variation 03 -->
<section class="variation" style="top:1272px">
<svg width="1200" height="588" viewBox="0 80 1000 490">
  <g class="dieline" transform="translate(17,0)">
    <text class="t-label t-bleed" x="60" y="101">Area di abbondanza/ <tspan font-style="italic">Background area</tspan></text>
    <text class="t-label t-cut" x="80" y="124">Linea di taglio/ <tspan font-style="italic">Cut line</tspan></text>
    <text class="t-label t-text" x="101" y="148">Area limite del testo/ <tspan font-style="italic">Text area</tspan></text>
    <text class="t-title" x="247" y="106">Color Variation -03</text>
    <line class="lead-bleed" x1="61" y1="104" x2="61" y2="168"/>
    <line class="lead-cut" x1="80" y1="127" x2="80" y2="176"/>
    <line class="lead-text" x1="101" y1="151" x2="101" y2="182"/>
    <rect x="43" y="168" width="571" height="115" fill="url(#g3)" role="img" aria-label="Flat cup wrap with sunset geometric shapes and dot textures"/>
    <rect class="bleed-edge" x="43" y="168" width="571" height="115"/>
    <rect class="text-area" x="58" y="182" width="542" height="88"/>
    <rect class="cut-line" x="51" y="176" width="556" height="100"/>
    <text class="t-micro" x="216" y="293">MADE IN ITALY ▪ C03 170cc G000000 PAPER</text>
    <path d="M85,372 Q335,290 587,348 L548,456 Q335,410 120,472 Z" fill="url(#g3)" stroke="#1a1a1a" stroke-width=".9" role="img" aria-label="Curved cup dieline with the sunset wrap pattern"/>
    <path class="fold-line" d="M92,386 Q335,305 578,362"/>
    <path class="fold-line" d="M118,462 Q335,400 548,446"/>
    <line class="paste-line" x1="572" y1="380" x2="548" y2="446"/>
    <g transform="translate(64,395) rotate(-20)"><rect class="pill" x="-14" y="-4" width="28" height="8" rx="4"/><text class="t-pill" y="1.5">Bleed Area</text></g>
    <text class="t-spec" x="347" y="487">6 OZ ICE CREAM/Desert CUP</text>
    <text class="t-spec" x="347" y="506">170 ml</text>
    <line x1="116" y1="524" x2="172" y2="524" stroke="#1a1a1a" stroke-width=".8" marker-end="url(#arrow-black)"/>
    <text class="t-legend" x="176" y="527" fill="#1a1a1a">CUTTING LINE</text>
    <line x1="246" y1="524" x2="302" y2="524" stroke="#c9302c" stroke-width=".8" marker-end="url(#arrow-red)"/>
    <text class="t-legend" x="306" y="527" fill="#c9302c">FOLDING LINE</text>
    <line x1="380" y1="524" x2="435" y2="524" stroke="#3aa84a" stroke-width=".8" marker-end="url(#arrow-green)"/>
    <text class="t-legend" x="440" y="527" fill="#3aa84a">PASTING SIDE</text>
  </g>
  <g class="showcase" transform="translate(-17,0)">
    <rect x="768" y="122" width="165" height="234" rx="18" fill="url(#m3)" role="img" aria-label="Three stacked dessert cups wearing the sunset wrap"/>
    <text class="t-palette" x="843" y="427">Syrup Sunset Pastel Color Palette</text>
    <rect x="777" y="437" width="27.5" height="91" fill="#f07660"/>
    <rect x="804.5" y="437" width="27.5" height="91" fill="#ee6278"/>
    <rect x="832" y="437" width="27.5" height="91" fill="#e64b83"/>
    <rect x="859.5" y="437" width="27.5" height="91" fill="#c4308a"/>
    <rect x="887" y="437" width="27.5" height="91" fill="#92278f"/>
  </g>
</svg>
</section>

<!-- Variation 04 -->
<section class="variation" style="top:1884px">
<svg width="1200" height="588" viewBox="0 80 1000 490">
  <g class="dieline">
    <text class="t-label t-bleed" x="60" y="101">Area di abbondanza/ <tspan font-style="italic">Background area</tspan></text>
    <text class="t-label t-cut" x="80" y="124">Linea di taglio/ <tspan font-style="italic">Cut line</tspan></text>
    <text class="t-label t-text" x="101" y="148">Area limite del testo/ <tspan font-style="italic">Text area</tspan></text>
    <text class="t-title" x="281" y="106">Color Variation -04</text>
    <line class="lead-bleed" x1="61" y1="104" x2="61" y2="168"/>
    <line class="lead-cut" x1="80" y1="127" x2="80" y2="176"/>
    <line class="lead-text" x1="101" y1="151" x2="101" y2="182"/>
    <rect x="43" y="168" width="571" height="115" fill="url(#g4)" role="img" aria-label="Flat cup wrap with candy-coloured geometric shapes and dot textures"/>
    <rect class="bleed-edge" x="43" y="168" width="571" height="115"/>
    <rect class="text-area" x="58" y="182" width="542" height="88"/>
    <rect class="cut-line" x="51" y="176" width="556" height="100"/>
    <text class="t-micro" x="216" y="293">MADE IN ITALY ▪ C03 170cc G000000 PAPER</text>
    <path d="M85,372 Q335,290 587,348 L548,456 Q335,410 120,472 Z" fill="url(#g4)" stroke="#1a1a1a" stroke-width=".9" role="img" aria-label="Curved cup dieline with the candy wrap pattern"/>
    <path class="fold-line" d="M92,386 Q335,305 578,362"/>
    <path class="fold-line" d="M118,462 Q335,400 548,446"/>
    <line class="paste-line" x1="572" y1="380" x2="548" y2="446"/>
    <g transform="translate(64,395) rotate(-20)"><rect class="pill" x="-14" y="-4" width="28" height="8" rx="4"/><text class="t-pill" y="1.5">Bleed Area</text></g>
    <g transform="translate(597,345) rotate(-65)"><rect class="pill" x="-16" y="-4" width="32" height="8" rx="4"/><text class="t-pill" y="1.5">Pasting Side</text></g>
    <g transform="translate(583,474) rotate(20)"><rect class="pill" x="-22" y="-4" width="44" height="8" rx="4"/><text class="t-pill" y="1.5">Non Printed Area</text></g>
    <text class="t-spec" x="347" y="487">6 OZ ICE CREAM/Desert CUP</text>
    <text class="t-spec" x="347" y="506">170 ml</text>
    <line x1="116" y1="524" x2="172" y2="524" stroke="#1a1a1a" stroke-width=".8" marker-end="url(#arrow-black)"/>
    <text class="t-legend" x="176" y="527" fill="#1a1a1a">CUTTING LINE</text>
    <line x1="246" y1="524" x2="302" y2="524" stroke="#c9302c" stroke-width=".8" marker-end="url(#arrow-red)"/>
    <text class="t-legend" x="306" y="527" fill="#c9302c">FOLDING LINE</text>
    <line x1="380" y1="524" x2="435" y2="524" stroke="#3aa84a" stroke-width=".8" marker-end="url(#arrow-green)"/>
    <text class="t-legend" x="440" y="527" fill="#3aa84a">PASTING SIDE</text>
  </g>
  <g class="showcase">
    <rect x="768" y="122" width="165" height="234" rx="18" fill="url(#m4)" role="img" aria-label="Three stacked dessert cups wearing the candy wrap"/>
    <text class="t-palette" x="845" y="427">Bright Candy Pastel Color Palette</text>
    <rect x="777" y="437" width="27.5" height="91" fill="#45a4dc"/>
    <rect x="804.5" y="437" width="27.5" height="91" fill="#74c25c"/>
    <rect x="832" y="437" width="27.5" height="91" fill="#f7ec57"/>
    <rect x="859.5" y="437" width="27.5" height="91" fill="#f8ac44"/>
    <rect x="887" y="437" width="27.5" height="91" fill="#ee3758"/>
  </g>
</svg>
</section>

<!-- Variation 05 (labelled -04) -->
<section class="variation" style="top:2500px">
<svg width="1200" height="588" viewBox="0 80 1000 490">
  <g class="dieline" transform="translate(17,0)">
    <text class="t-label t-bleed" x="60" y="101">Area di abbondanza/ <tspan font-style="italic">Background area</tspan></text>
    <text class="t-label t-cut" x="80" y="124">Linea di taglio/ <tspan font-style="italic">Cut line</tspan></text>
    <text class="t-label t-text" x="101" y="148">Area limite del testo/ <tspan font-style="italic">Text area</tspan></text>
    <text class="t-title" x="247" y="106">Color Variation -04</text>
    <line class="lead-bleed" x1="61" y1="104" x2="61" y2="168"/>
    <line class="lead-cut" x1="80" y1="127" x2="80" y2="176"/>
    <line class="lead-text" x1="101" y1="151" x2="101" y2="182"/>
    <rect x="43" y="168" width="571" height="115" fill="url(#g5)" role="img" aria-label="Flat cup wrap with twitch pastel geometric shapes and grid textures"/>
    <rect class="bleed-edge" x="43" y="168" width="571" height="115"/>
    <rect class="text-area" x="58" y="182" width="542" height="88"/>
    <rect class="cut-line" x="51" y="176" width="556" height="100"/>
    <text class="t-micro" x="216" y="293">MADE IN ITALY ▪ C03 170cc G000000 PAPER</text>
    <path d="M85,372 Q335,290 587,348 L548,456 Q335,410 120,472 Z" fill="url(#g5)" stroke="#1a1a1a" stroke-width=".9" role="img" aria-label="Curved cup dieline with the twitch pastel wrap pattern"/>
    <path class="fold-line" d="M92,386 Q335,305 578,362"/>
    <path class="fold-line" d="M118,462 Q335,400 548,446"/>
    <line class="paste-line" x1="572" y1="380" x2="548" y2="446"/>
    <g transform="translate(64,395) rotate(-20)"><rect class="pill" x="-14" y="-4" width="28" height="8" rx="4"/><text class="t-pill" y="1.5">Bleed Area</text></g>
    <text class="t-spec" x="347" y="487">6 OZ ICE CREAM/Desert CUP</text>
    <text class="t-spec" x="347" y="506">170 ml</text>
    <line x1="116" y1="524" x2="172" y2="524" stroke="#1a1a1a" stroke-width=".8" marker-end="url(#arrow-black)"/>
    <text class="t-legend" x="176" y="527" fill="#1a1a1a">CUTTING LINE</text>
    <line x1="246" y1="524" x2="302" y2="524" stroke="#c9302c" stroke-width=".8" marker-end="url(#arrow-red)"/>
    <text class="t-legend" x="306" y="527" fill="#c9302c">FOLDING LINE</text>
    <line x1="380" y1="524" x2="435" y2="524" stroke="#3aa84a" stroke-width=".8" marker-end="url(#arrow-green)"/>
    <text class="t-legend" x="440" y="527" fill="#3aa84a">PASTING SIDE</text>
  </g>
  <g class="showcase" transform="translate(-17,0)">
    <rect x="768" y="122" width="165" height="234" rx="18" fill="url(#m5)" role="img" aria-label="Three stacked dessert cups wearing the twitch pastel wrap"/>
    <text class="t-palette" x="845" y="427">Twitch Pastel Color Palette</text>
    <rect x="777" y="437" width="27.5" height="91" fill="#7b71b8"/>
    <rect x="804.5" y="437" width="27.5" height="91" fill="#f7eaf4"/>
    <rect x="832" y="437" width="27.5" height="91" fill="#f05d5e"/>
    <rect x="859.5" y="437" width="27.5" height="91" fill="#fed47e"/>
    <rect x="887" y="437" width="27.5" height="91" fill="#2e9a8e"/>
  </g>
</svg>
</section>

</body>
</html>
```